Business Card for Maplethorne Elder Keepers

I need a business card design for a very elite and personalized companion care company. We take care of the client at home with respect, dignity, and our full attention. The design should communicate a classic elegance and trust.

/Users/lorafenwick/Downloads/graphwellhub_121488_23943024_3826329_sourcefile

```html
<!DOCTYPE html>
<html lang="en">
<head>
<meta charset="utf-8">
<title>Maplethorne Elder Keepers – Business Card</title>
<link href="https://fonts.googleapis.com/css2?family=Cinzel:wght@500;700&family=Crimson+Text:wght@400&display=swap" rel="stylesheet">
<style>
  :root {
    --navy: #1d4c87;
    --navy-deep: #18437a;
    --sky: #3fbbec;
    --paper: #ffffff;
    --backdrop: #2b2b2d;
  }
  * { margin: 0; padding: 0; box-sizing: border-box; }
  html, body { width: 1200px; height: 900px; overflow: hidden; background: var(--backdrop); }
  .stage { width: 1200px; height: 900px; display: flex; align-items: center; justify-content: center; }
  .card {
    position: relative;
    width: 1000px; height: 572px;
    background: var(--paper);
    overflow: hidden;
  }
  .card__wave { position: absolute; inset: 0; width: 100%; height: 100%; }
  .brand {
    position: absolute; left: 92px; top: 58px;
    font-family: "Cinzel", serif; font-weight: 700;
    color: var(--navy);
    line-height: 1.02;
    display: flex; align-items: center; gap: 16px;
  }
  .brand__dot { width: 18px; height: 18px; border-radius: 50%; background: var(--navy); flex: none; }
  .brand__name { font-size: 40px; letter-spacing: 1px; }
  .brand__name span { display: block; font-size: 27px; letter-spacing: 3px; }
  .address {
    position: absolute; left: 92px; top: 190px;
    font-family: "Crimson Text", serif; font-size: 21px; line-height: 1.3;
    font-style: normal;
    color: var(--navy);
  }
  .person {
    position: absolute; right: 60px; top: 118px; text-align: right;
    font-family: "Cinzel", serif;
  }
  .person__name { font-size: 28px; font-weight: 700; color: var(--navy); letter-spacing: 1px; }
  .person__role { font-size: 19px; font-weight: 500; color: var(--sky); letter-spacing: 1px; margin-top: 4px; }
  .contact {
    position: absolute; right: 60px; bottom: 40px;
    list-style: none;
    font-family: "Crimson Text", serif; font-size: 21px; color: var(--paper);
  }
  .contact li { display: flex; align-items: center; justify-content: flex-end; gap: 14px; line-height: 1.5; }
  .contact svg { width: 18px; height: 18px; fill: var(--sky); flex: none; }
</style>
</head>
<body>
<main class="stage">
  <article class="card">
    <svg class="card__wave" viewBox="0 0 1000 572" preserveAspectRatio="none" aria-hidden="true">
      <path fill="var(--sky)" d="M0,355 C150,415 400,428 560,400 C400,430 150,440 0,412 Z"/>
      <path fill="var(--navy)" d="M200,330 C330,390 520,390 700,330 C820,290 920,230 1000,175 L1000,190 C920,248 820,305 700,345 C520,400 330,395 200,330 Z"/>
      <path fill="var(--navy-deep)" d="M0,445 C300,445 620,420 800,340 C900,295 960,255 1000,230 L1000,572 L0,572 Z"/>
    </svg>

    <div class="brand">
      <span class="brand__dot"></span>
      <div class="brand__name">Maplethorne<span>Elder Keepers</span></div>
    </div>

    <address class="address">
      418 Linden Crescent NW<br>
      Suite 210, Harbor Falls<br>
      MI 49188
    </address>

    <div class="person">
      <div class="person__name">Theodore Ashcombe</div>
      <div class="person__role">CEO/Founder</div>
    </div>

    <ul class="contact">
      <li>214 555 0148
        <svg viewBox="0 0 24 24"><path d="M6.6 10.8a15 15 0 0 0 6.6 6.6l2.2-2.2a1 1 0 0 1 1-.25 11.4 11.4 0 0 0 3.6.57 1 1 0 0 1 1 1V20a1 1 0 0 1-1 1A17 17 0 0 1 3 4a1 1 0 0 1 1-1h3.5a1 1 0 0 1 1 1c0 1.25.2 2.45.57 3.57a1 1 0 0 1-.25 1z"/></svg>
      </li>
      <li>214 555 0148
        <svg viewBox="0 0 24 24"><path d="M6 2h12v5H6zM4 8h16a2 2 0 0 1 2 2v7h-4v5H6v-5H2v-7a2 2 0 0 1 2-2zm4 8v4h8v-4z"/></svg>
      </li>
      <li>theo@maplethornekeepers.com
        <svg viewBox="0 0 24 24"><path d="M2 5h20v14H2zm2 2v.5l8 5 8-5V7z"/></svg>
      </li>
      <li>www.maplethornekeepers.com
        <svg viewBox="0 0 24 24"><path d="M12 2a10 10 0 1 0 0 20 10 10 0 0 0 0-20zm6.9 9h-3a15 15 0 0 0-1.3-5.6A8 8 0 0 1 18.9 11zM12 4c.9 1.2 1.8 3.7 1.9 7h-3.8c.1-3.3 1-5.8 1.9-7zM9.4 5.4A15 15 0 0 0 8.1 11h-3a8 8 0 0 1 4.3-5.6zM5.1 13h3a15 15 0 0 0 1.3 5.6A8 8 0 0 1 5.1 13zM12 20c-.9-1.2-1.8-3.7-1.9-7h3.8c-.1 3.3-1 5.8-1.9 7zm2.6-1.4a15 15 0 0 0 1.3-5.6h3a8 8 0 0 1-4.3 5.6z"/></svg>
      </li>
    </ul>
  </article>
</main>
</body>
</html>
```